Flyer To Solicit Donations for a Good Cause

Hi. I am running the distance of a marathon race to solicit donations for a charitable cause. I need a well designed flyer to help me solicit support from friends and others. The copy for the flyer is attached. There is a significant amount of written text so it will need to be laid out in a way that is easy to read but also mixes well with some good images and design appeal. I am open to creative ideas. I have also attached my photo and a photo of me shaking hands with Mayor Velidis of Delphi and president of the Concordant Aegean Fellowship. Also there are some photos of the areas. These photos don't have to be used except for the one of me shaking hands with the Mayor and a caption underneath it. Otherwise, I am open to other stock photos or graphics. Feel free to contact me if you have questions. Thank you !

Update: ONE SIDED FLYER

Requirements
Must have
• Photo of the Mayor and Dale with the caption identifying us; All of the copy/text.

```html
<!DOCTYPE html>
<html lang="en">
<head>
<meta charset="utf-8">
<title>A Special Journey – Prayer Run Flyer</title>
<link href="https://fonts.googleapis.com/css2?family=Anton&family=Archivo+Black&family=Lato:wght@300;400;900&family=Patrick+Hand&family=Poppins:wght@200&family=Roboto+Condensed:ital,wght@0,300;0,400;0,700;1,400;1,700&display=swap" rel="stylesheet">
<style>
  :root {
    --ink: #000;
    --paper: #fff;
    --red: #d7242e;
    --sky: #19ade6;
    --yellow: #fff200;
    --gold: #f2ea1d;
    --green: #3aad4a;
    --navy: #263f93;
    --photo-wall: #c9d4dc;
  }
  * { box-sizing: border-box; margin: 0; padding: 0; }
  html, body { width: 846px; height: 1200px; overflow: hidden; background: var(--paper); }
  .flyer { position: relative; width: 846px; height: 1200px; overflow: hidden; font-family: "Roboto Condensed", sans-serif; }
  .shapes { position: absolute; inset: 0; }
  .abs { position: absolute; }

  .title {
    left: 40px; width: 766px; top: 28px; text-align: center;
    font-family: "Poppins", sans-serif; font-weight: 200; font-size: 70px;
    color: var(--red); letter-spacing: 1px; line-height: 1; white-space: nowrap;
  }
  .headline {
    left: 0; width: 846px; top: 108px; text-align: center;
    font-family: "Anton", sans-serif; color: var(--paper);
    font-size: 50px; line-height: 56px; text-transform: uppercase;
  }
  .intro {
    left: 43px; top: 246px; width: 420px; white-space: nowrap;
    font-family: "Lato", sans-serif; font-weight: 300; font-size: 24px; line-height: 34px; color: var(--paper);
  }
  .intro b { font-weight: 900; color: var(--ink); }
  .intro .hl { font-weight: 900; color: var(--yellow); }

  .sponsor-box {
    left: 20px; top: 480px; width: 388px; height: 188px;
    border: 2px solid var(--sky); background: var(--paper);
    padding: 4px 6px 0; text-align: center;
    font-family: "Patrick Hand", cursive; font-size: 19.5px; line-height: 26px;
  }
  .sponsor-link {
    display: block; margin: 3px auto 0; width: 300px;
    background: var(--sky); color: var(--paper);
    font-family: "Roboto Condensed", sans-serif; font-weight: 700; font-size: 16px; line-height: 24px;
  }

  .handshake-frame {
    left: 480px; top: 238px; width: 304px; height: 334px;
    background: var(--red); transform: rotate(4deg); padding: 10px 12px 0;
  }
  .handshake-photo {
    width: 280px; height: 282px;
    background: linear-gradient(180deg, #9fb9d3 0%, var(--photo-wall) 45%, #d9d2c8 70%, #8c3b34 100%);
  }
  .handshake-caption {
    color: var(--paper); text-align: center; font-size: 14px; line-height: 17px; font-weight: 700; padding-top: 7px;
  }

  .concept-head {
    left: 440px; width: 384px; top: 602px; text-align: center;
    font-family: "Anton", sans-serif; color: var(--yellow); font-size: 20px;
  }
  .concept-body {
    left: 440px; width: 384px; top: 638px; text-align: center;
    font-style: italic; color: var(--paper); font-size: 17.5px; line-height: 24px;
  }

  .banner { left: 32px; top: 700px; width: 776px; height: 132px; transform: rotate(-3deg); background: var(--yellow); }
  .banner-text { position: absolute; inset: 0; text-align: center; font-family: "Roboto Condensed", sans-serif; font-style: italic; }
  .banner-main { font-family: "Archivo Black", sans-serif; font-size: 23px; line-height: 34px; padding-top: 8px; white-space: nowrap; letter-spacing: -0.3px; }
  .banner-sub { font-size: 17px; line-height: 22px; font-weight: 700; }
  .banner-note { color: var(--red); font-size: 17px; line-height: 22px; }

  .call {
    left: 40px; width: 770px; top: 852px; text-align: center;
    font-family: "Archivo Black", sans-serif; font-style: italic; color: var(--paper);
    font-size: 23px; line-height: 34px;
  }

  .steps { left: 22px; top: 933px; width: 400px; list-style: none; }
  .step { color: var(--paper); font-size: 16px; font-weight: 300; line-height: 21px; padding: 0 4px; margin-bottom: 6px; }
  .step--contact { background: var(--navy); padding-bottom: 4px; }
  .step--decide { background: var(--sky); }
  .step--define { background: var(--red); }
  .step--refine { background: var(--green); }
  .step b { font-weight: 700; }

  .donation {
    left: 430px; top: 932px; width: 400px; height: 134px;
    background: var(--ink); color: var(--gold); font-size: 16px; font-weight: 300; line-height: 21.5px; padding: 1px 6px;
  }
  .closing {
    left: 430px; width: 400px; top: 1090px; text-align: center;
    font-family: "Archivo Black", sans-serif; font-size: 19.5px; line-height: 27px;
  }
</style>
</head>
<body>
<main class="flyer">
  <svg class="shapes" width="846" height="1200" viewBox="0 0 846 1200" aria-hidden="true">
    <rect x="0" y="0" width="846" height="232" fill="var(--ink)"/>
    <polygon points="120,0 846,0 846,24 800,98 64,98" fill="var(--paper)"/>
    <polygon points="0,232 424,232 488,288 400,456 0,456" fill="var(--sky)"/>
    <polygon points="0,464 404,464 486,296 416,676 0,700" fill="var(--paper)" stroke="var(--sky)" stroke-width="3"/>
    <polygon points="470,600 824,556 824,844 20,844 20,704 430,704" fill="var(--ink)"/>
    <polygon points="40,848 810,848 824,884 810,920 40,920 24,884" fill="var(--red)"/>
  </svg>

  <h1 class="abs title">A SPECIAL JOURNEY</h1>
  <h2 class="abs headline">For your specific prayers &amp;<br>for an important ancient cause</h2>

  <p class="abs intro">This coming April 2016 <b>Dale</b><br><b>Merrow</b> will make a special<br>running <span class="hl">journey of 26 miles</span><br>through the ancient lands of<br><b>Apollo and Athena</b> at Delphi<br>on Mt. Parnassus in Greece.</p>

  <div class="abs sponsor-box">
    Dale will adorn his running outfit with special cloth<br>strips that will contain written prayers and petitions<br>of people who will sponsor his journey by making a<br>charitable donation to the Concordant Aegean Fellowship,<br>an organization that preserves the land and the<br>Delphic culture.
    <span class="sponsor-link">www.aegean-fellowship-committee.org</span>
  </div>

  <figure class="abs handshake-frame">
    <div class="handshake-photo" role="img" aria-label="Photo of Dale shaking hands with Mayor Velidis in an office in front of a large wall map"></div>
    <figcaption class="handshake-caption">Dale Merrow with Mayor Velidis of Delphi</figcaption>
  </figure>

  <p class="abs concept-head">THE CONCEPT IS SIMPLE AND VERY POWERFUL:</p>
  <p class="abs concept-body">as Dale runs, your written prayer on a cloth strip<br>will flow and emanate in the wind</p>

  <div class="abs banner">
    <div class="banner-text">
      <p class="banner-main">being blessed by the spirits of this ancient and magical land</p>
      <p class="banner-sub">asking unto the wind that your prayer be answered.</p>
      <p class="banner-note">This type of prayer practice dates back to ancient times. The Tibetan culture<br>commonly uses prayer flags with special mantras and symbols.</p>
    </div>
  </div>

  <p class="abs call">Will you make a prayer for yourself or a loved and support a<br>good cause? Here is how to get your prayer started:</p>

  <ol class="abs steps">
    <li class="step step--decide">Decide what you want your prayer, petition or intention to be.</li>
    <li class="step step--define">Define your prayer, petition or intention by writing it down.</li>
    <li class="step step--refine">Refine it is concise, clear &amp; specific. (18 words or less is ideal for each strip cloth).</li>
    <li class="step step--contact">Contact Dale at <b>dmerrow@merrowlane.com</b> and tell him how many prayer cloth strips you wish to obtain. Dale will then send you the cloth for you to write your prayer and send back to him or he will write out the prayer for you. Dale can also answer any questions you may have.</li>
  </ol>

  <p class="abs donation">A minimum donation of $50 for each prayer cloth is requested. Checks can be made to the “Merrow Lane Trust Account/Concordant Aegean Fellowship” and mail to Dale T. Merrow, Merrow Lane PLC, 4815 Orchard Row, Ste. 210 Fairhaven, Virginia 23399 or though online payment instructions sent by email from Dale as requested.</p>

  <p class="abs closing">Your Prayer Can Make A Difference<br>For You &amp; For A Good Cause !</p>
</main>
</body>
</html>
```